Stylist/Barber Standup Sign for Hair Regrowth Company

We want to design an attractive and eye-catching sign for hair stylists and barbers to sit on their workstations to attract the attention of their clients regarding hair loss and encourage them to speak to their stylist about it of they are would like to seek treatment.
50% of men and 25% of women suffer from hair loss but most are in denial that it is happening or too embarrassed to talk about it.

Copy for the flyer is as follows:

[Section 1:]
This flyer has been placed here/designed to spark conversation about hair loss

[Section 2:]
The truth is...
73% of people believe their hair is thinning
They are right

[Section 3:]
If you've got questions, your stylist or barber has answers.

Additional Background Information:

Primary target audience is men between the ages of 25-45, secondary target audience is men 46-60

Current Consumer Perception? (in the first person) “I’ve been thinking about my hair. I think it’s getting thinner and I’m scared, worried and don’t know what to do. But I don’t know if there is anything that really works. I’ve tried other things and nothing‘s worked.”

Tonality of materials? Very guy friendly, matter of fact, authoritative, its what you might hear from your best friend. Confident. Encouraging, but with a sense of urgency.

Please use our brand colors, but do not include our logo or brand name.
Colors are as follows:
Green: #4ca26f
Light Grey: #999999
Dark Grey: #262626

I have attached print templates in both PDF and Jpeg, please use those to provide final ready to print documents if you are selected.

Target Market(s)

Industry/Entity Type

Health And Wellness

Font styles to use
Sans Serif

Colors
00a990
ffffff
333333
cbcbcb

Requirements
Must have
• We want to get across the following messaging. Ideally you will submit a design using our copy and if you think you can do better, please feel free to submit another design with your own copy/messaging. If you can do it better we would love to select you :-)
• Our copy?
• This flyer has been placed here/designed to spark conversation about hair loss
• The truth is...
• 73% of people believe their hair is thinning
• They are right
• If you've got questions, your stylist or barber has answers
• Also please use our brand colors:
• Green: #4ca26f
• Light Grey: #999999
• Dark Grey: #262626
Should not have
• dont add any logos, images or ornate design. this needs to be simple, easy to ready and eye catching.
• do not use the color red in any capacity.

```html
<!DOCTYPE html>
<html lang="en">
<head>
<meta charset="UTF-8">
<title>Hair Loss Conversation Sign</title>
<link href="https://fonts.googleapis.com/css2?family=Lato:wght@400;700;900&family=Montserrat:wght@500;600&display=swap" rel="stylesheet">
<style>
  :root {
    --green: #4ca26f;
    --dark: #262626;
    --grey: #999999;
    --light-grey: #b5b5b5;
    --paper: #f4f4f2;
    --stage: #e6e6ea;
  }
  * { margin: 0; padding: 0; box-sizing: border-box; }
  html, body { width: 1200px; height: 980px; overflow: hidden; background: var(--stage); }
  .sign {
    position: absolute; left: 250px; top: 15px;
    width: 700px; height: 950px;
    background: var(--paper);
    overflow: hidden;
    font-family: "Lato", sans-serif;
    color: var(--dark);
  }
  .sign-art { position: absolute; inset: 0; }
  .stat { position: absolute; font-family: "Montserrat", sans-serif; line-height: 1; }
  .stat-figure { font-size: 118px; font-weight: 600; letter-spacing: -3px; }
  .stat-label { font-size: 42px; font-weight: 500; letter-spacing: -1px; }
  .stat-men { left: 50px; top: 372px; text-align: right; width: 280px; }
  .stat-men .stat-figure { color: var(--dark); }
  .stat-men .stat-label { color: var(--green); margin-top: 4px; }
  .stat-women { left: 370px; top: 406px; width: 300px; text-align: right; }
  .stat-women .stat-figure { color: var(--green); }
  .stat-women .stat-label { color: var(--dark); margin-top: 4px; }
  .stat-divider { position: absolute; left: 345px; top: 372px; width: 1.5px; height: 200px; background: var(--grey); }
  .rule { position: absolute; left: 20px; right: 20px; height: 1.5px; background: var(--dark); }
  .rule-top { top: 584px; }
  .subhead {
    position: absolute; left: 20px; right: 20px; top: 594px;
    text-align: center; font-weight: 700; font-size: 20px; line-height: 1.25;
  }
  .facts { position: absolute; left: 0; right: 0; top: 665px; height: 185px; display: flex; }
  .facts::before { content: ""; position: absolute; left: 0; right: 0; top: -6px; height: 6px; background: var(--green); }
  .facts::after { content: ""; position: absolute; left: 0; right: 0; bottom: -6px; height: 6px; background: var(--dark); }
  .truth { width: 53%; background: var(--dark); color: #fff; padding: 22px 30px; }
  .truth-title { font-weight: 900; font-size: 44px; line-height: 1.05; margin-bottom: 10px; }
  .truth-copy { font-size: 22px; line-height: 1.2; }
  .answers { flex: 1; background: var(--green); color: #fff; position: relative; padding: 40px 30px; }
  .answers-copy { font-size: 23px; line-height: 1.2; width: 180px; }
  .answers-mark {
    position: absolute; right: 28px; top: 2px;
    font-family: "Montserrat", sans-serif; font-weight: 600; font-size: 170px; line-height: 1;
    color: #fff; text-shadow: 3px 3px 0 rgba(0,0,0,0.25);
  }
  .conversation { position: absolute; left: 0; right: 0; top: 858px; bottom: 0; }
  .bubbles { position: absolute; left: 45px; top: 10px; }
  .conversation-copy {
    position: absolute; left: 210px; right: 30px; top: 22px;
    text-align: center; font-weight: 700; font-size: 23px; line-height: 1.2;
  }
</style>
</head>
<body>
<main class="sign">
  <svg class="sign-art" width="700" height="950" viewBox="0 0 700 950">
    <defs>
      <linearGradient id="photoTone" x1="0" y1="0" x2="1" y2="1">
        <stop offset="0" stop-color="#cfdde3"/>
        <stop offset="0.5" stop-color="#d9c4b2"/>
        <stop offset="1" stop-color="#e7e5cf"/>
      </linearGradient>
    </defs>
    <rect class="photo" x="0" y="0" width="700" height="420" fill="url(#photoTone)" role="img" aria-label="Photo of a man and a woman worriedly checking their thinning hair"/>
    <path class="wave-green" d="M0 300 C 120 230, 250 270, 400 300 S 620 370, 700 365" fill="none" stroke="var(--green)" stroke-width="7"/>
    <path class="wave-grey" d="M0 312 C 120 242, 250 282, 400 312 S 620 382, 700 377" fill="none" stroke="var(--grey)" stroke-width="5"/>
    <path class="panel" d="M0 330 C 120 260, 250 300, 400 330 S 620 400, 700 395 L700 950 L0 950 Z" fill="var(--paper)"/>
    <path class="wave-dark" d="M0 330 C 120 260, 250 300, 400 330 S 620 400, 700 395" fill="none" stroke="var(--dark)" stroke-width="6"/>
  </svg>

  <div class="stat stat-men">
    <div class="stat-figure">50%</div>
    <div class="stat-label">OF MEN</div>
  </div>
  <div class="stat-divider"></div>
  <div class="stat stat-women">
    <div class="stat-figure">25%</div>
    <div class="stat-label">OF WOMEN</div>
  </div>

  <div class="rule rule-top"></div>
  <p class="subhead">Suffer From Hair Loss But Most Are In Denial That It Is<br>Happening Or Too Embarrassed To Talk About It.</p>

  <section class="facts">
    <div class="truth">
      <h2 class="truth-title">The Truth is...</h2>
      <p class="truth-copy">73% of people believe<br>their hair is thinning<br>They are right</p>
    </div>
    <div class="answers">
      <p class="answers-copy">If you've got questions, your stylist or barber has answers</p>
      <span class="answers-mark">?</span>
    </div>
  </section>

  <section class="conversation">
    <svg class="bubbles" width="140" height="85" viewBox="0 0 140 85" aria-hidden="true">
      <path d="M72 18 h48 a18 18 0 0 1 18 18 v14 a18 18 0 0 1 -18 18 h-2 l8 14 l-22 -14 h-32 a18 18 0 0 1 -18 -18 v-14 a18 18 0 0 1 18 -18 z" fill="var(--light-grey)" stroke="var(--paper)" stroke-width="3"/>
      <path d="M24 2 h54 a22 22 0 0 1 22 22 v10 a22 22 0 0 1 -22 22 h-38 l-26 16 l8 -16 a22 22 0 0 1 -20 -22 v-10 a22 22 0 0 1 22 -22 z" fill="var(--light-grey)" stroke="var(--paper)" stroke-width="3"/>
    </svg>
    <p class="conversation-copy">This flyer has been placed here/designed<br>to spark conversation about hair loss</p>
  </section>
</main>
</body>
</html>
```